TRU PEAK POWER.

I'd like my business logo.
contact name: Desmond Halvik
phone:0438275160
email: info@trupeakpower.net.au
website: www.trupeakpower.net.au

services:
solar
battery storage
LED lighting
energy saving solutions
general electrical
I'd like the design to look professional

Target Market(s)

Everyone

Industry/Entity Type

Business

Contact Information for Business Card

as described above

Requirements
Must have
• Id like the colours and the design to work well with my logo.

```html
<!DOCTYPE html>
<html lang="en">
<head>
<meta charset="utf-8">
<title>Tru Peak Power – Business Card</title>
<link rel="stylesheet" href="https://fonts.googleapis.com/css2?family=Arimo:wght@400;700&display=swap">
<style>
  :root {
    --forest: #3f702a;
    --lime: #7ac143;
    --sun: #f5a21b;
    --brand: #4e9a2e;
    --ink: #1d1d1d;
    --paper: #ffffff;
    --backdrop: #f0f0ee;
  }
  * { margin: 0; padding: 0; box-sizing: border-box; }
  html, body {
    width: 1200px; height: 786px; overflow: hidden;
    background: var(--backdrop);
    font-family: "Arimo", Arial, sans-serif;
  }
  .card {
    position: absolute; left: 120px; top: 100px;
    width: 960px; height: 587px;
    background: var(--paper);
    overflow: hidden;
    box-shadow: 0 6px 24px rgba(0,0,0,0.12);
  }
  .card-bands { position: absolute; inset: 0; }
  .contact-name {
    position: absolute; left: 56px; top: 306px;
    color: var(--paper); font-size: 27px; font-weight: 700;
  }
  .contact-list { position: absolute; left: 57px; top: 412px; list-style: none; }
  .contact-item {
    display: flex; align-items: center; height: 30px; margin-bottom: 19px;
    color: var(--paper); font-size: 19px;
  }
  .contact-key {
    width: 32px; height: 28px; margin-right: 12px;
    background: var(--lime); color: var(--paper);
    font-size: 15px; font-weight: 700;
    display: flex; align-items: center; justify-content: center;
  }
  .brand {
    position: absolute; left: 370px; top: 188px; width: 480px;
    display: flex; align-items: center; justify-content: center; gap: 16px;
  }
  .brand-dot { width: 44px; height: 44px; border-radius: 50%; background: var(--sun); flex: none; }
  .brand-name {
    color: var(--brand); font-size: 44px; font-weight: 700; letter-spacing: 1px; white-space: nowrap;
  }
  .services { position: absolute; left: 400px; top: 366px; width: 526px; text-align: center; }
  .services-label {
    display: inline-block; background: var(--lime); color: var(--paper);
    font-size: 19px; font-weight: 700; padding: 3px 8px; margin-bottom: 10px;
  }
  .services-list { color: var(--ink); font-size: 20px; line-height: 31px; }
</style>
</head>
<body>
  <div class="card">
    <svg class="card-bands" width="960" height="587" viewBox="0 0 960 587" aria-hidden="true">
      <polygon points="0,0 304,0 434,587 0,587" fill="var(--lime)"/>
      <polygon points="0,0 294,0 424,587 0,587" fill="var(--forest)"/>
      <polygon points="815,0 960,0 960,587 947,587" fill="var(--lime)"/>
      <polygon points="825,0 960,0 960,587 957,587" fill="var(--forest)"/>
    </svg>

    <div class="contact-name">Desmond Halvik</div>
    <ul class="contact-list">
      <li class="contact-item"><span class="contact-key">p</span>0438275160</li>
      <li class="contact-item"><span class="contact-key">e</span>info@trupeakpower.net.au</li>
      <li class="contact-item"><span class="contact-key">w</span>www.trupeakpower.net.au</li>
    </ul>

    <div class="brand">
      <span class="brand-dot"></span>
      <span class="brand-name">TRU PEAK POWER</span>
    </div>

    <div class="services">
      <span class="services-label">Our Services:</span>
      <p class="services-list">Solar Battery Storage, LED Lighting,<br>Energy Saving Solutions, General Electrical</p>
    </div>
  </div>
</body>
</html>
```